Green Logistics / Last Mile Delivery Firm needs cool one-page website

FYI - We do have a detailed brief in the uploaded files section below
COMPANY
We recently launched the company Brook Logistics which is a pioneer in urban green logistics and provides zero-emissions last mile delivery services (i.e. delivery of parcels with delivery vans to the doorstep of households) for its logistics and retail clients.
We take on urban parcel delivery for our clients with a 100% electric commercial vehicles fleet, fair and sustainable working conditions for our employees and an unparalleled professional and customer-focused mindset.
WEBSITE
In the detailed brief, we have provided examples to emulate. We need the design + coding of the website. Website needs to be friendly/optimized for and should open swiftly on both Android & iOS.
In general, the website should convey
- green mission of the company
- sustainability (good working conditions, focus on employees)
- customer orientation
- professionalism
DESIGN
In the detailed brief, we have provided designs to emulate.
Color design: we do have a logo which features 2 green colors (one lighter and one darker color tone). However, the colors on the website do not necessarily need to follow these 2 colors exactly as we are able to switch the logo colors.
Imagery: should reflect maybe 50% green/leaf/tree , 25% customer and employee orientation, and 25% logistics (here it's important that it is the last mile delivery, i.e. delivery with delivery vans to the doorstep of households)
Coding

```html
<!DOCTYPE html>
<html lang="en">
<head>
<meta charset="utf-8">
<title>Brook Logistics – Clean Last Mile Delivery</title>
<link href="https://fonts.googleapis.com/css2?family=Roboto+Condensed:wght@400;700&family=Lato:wght@400;700&display=swap" rel="stylesheet">
<style>
:root{
  --green-dark:#1f8f3a;
  --green-light:#8dc63f;
  --green-mid:#2a9a3f;
  --ink:#222;
  --text:#444;
  --card:#f0f0f0;
  --white:#fff;
  --line:#dcdcdc;
}
*{box-sizing:border-box;margin:0;padding:0}
html,body{width:1200px;height:4431px;overflow:hidden;background:var(--white)}
body{font-family:'Lato',sans-serif;color:var(--text);position:relative}
.abs{position:absolute}
h1,h2,h3,h4,.cond{font-family:'Roboto Condensed',sans-serif}
.section-title{position:absolute;left:0;width:1200px;text-align:center;font-size:31px;font-weight:700;color:var(--ink);letter-spacing:.3px}
.section-title::after{content:"";display:block;width:50px;height:4px;background:var(--green-dark);margin:14px auto 0}
.brand{font-family:'Lato',sans-serif;font-weight:700;color:var(--green-dark);display:flex;align-items:center;gap:12px;white-space:nowrap}
.brand-dot{width:40px;height:40px;border-radius:50%;background:var(--green-light);flex:none}
.btn{position:absolute;display:flex;align-items:center;justify-content:center;border-radius:30px;background:var(--green-light);color:var(--white);font-family:'Roboto Condensed',sans-serif;font-weight:700;font-size:17px}

/* header */
.site-header{position:absolute;left:0;top:0;width:1200px;height:108px;background:var(--white)}
.site-header .brand{position:absolute;left:74px;top:34px;font-size:24px}
.main-nav{position:absolute;left:576px;top:42px;display:flex;align-items:center;font-size:15px;font-weight:700;color:var(--ink)}
.main-nav span{margin-right:38px}
.main-nav .active{background:var(--green-light);color:var(--white);padding:9px 22px;border-radius:22px;margin-left:-16px;margin-right:18px}

/* hero */
.hero{position:absolute;left:0;top:108px;width:1200px;height:571px;background:linear-gradient(100deg,#8c8b88 0%,#d8d8d6 30%,#ececea 55%,#9a9690 80%,#6f6a63 100%)}
.hero h1{position:absolute;left:0;width:1200px;text-align:center;color:var(--white);font-size:52px;line-height:48px;top:176px;text-shadow:0 2px 6px rgba(0,0,0,.35)}
.hero .tagline{position:absolute;left:0;width:1200px;top:278px;text-align:center;color:var(--white);font-weight:700;font-size:33px;text-shadow:0 2px 6px rgba(0,0,0,.35)}
.hero .btn{left:518px;top:341px;width:164px;height:48px}
.dots{position:absolute;left:483px;top:522px;display:flex;gap:11px}
.dots i{display:block;width:30px;height:5px;background:var(--white);border-radius:3px}
.dots i:first-child{background:var(--green-light)}

/* about */
.about-card{position:absolute;top:877px;width:331px;height:443px;background:var(--card);border-radius:0 0 22px 22px;text-align:center;padding:110px 26px 0}
.about-card .icon{position:absolute;left:110px;top:-49px;width:111px;height:111px;border-radius:50%;background:var(--green-dark);border:5px solid var(--white);display:flex;align-items:center;justify-content:center}
.about-card h3{font-size:22px;color:var(--green-dark);margin-bottom:12px}
.about-card p{font-size:14px;line-height:24px;margin-bottom:10px}

/* is / is not */
.split-left{position:absolute;left:0;top:1375px;width:600px;height:645px;background:var(--green-dark)}
.split-right{position:absolute;left:600px;top:1375px;width:600px;height:645px;background:var(--green-light)}
.is-pill{position:absolute;left:394px;top:1440px;width:412px;height:43px;border-radius:22px;background:var(--white);color:var(--ink);font-size:30px;font-weight:700;display:flex;align-items:center;justify-content:center}
.divider{position:absolute;left:598px;top:1483px;width:4px;height:150px;background:var(--white)}
.divider-dot{position:absolute;left:566px;top:1616px;width:68px;height:68px;border-radius:50%;border:4px solid var(--white);background:var(--green-dark)}
.list{position:absolute;color:var(--white);font-size:16px}
.list h4{font-size:17px;height:30px;line-height:22px}
.list li{list-style:none;display:flex;align-items:center;gap:14px;height:39.5px}
.list li svg{flex:none}
.list.struck h4,.list.struck li span{text-decoration:line-through}
.van-art{position:absolute;left:120px;top:1772px;width:376px;height:185px;border-radius:40px 90px 20px 20px;background:linear-gradient(#fff,#d9d9d9)}
.split-right .brand{position:absolute;left:70px;top:470px;font-size:34px;color:var(--white)}
.split-right .brand-dot{width:70px;height:70px;background:var(--white)}

/* services */
.services-intro{position:absolute;left:74px;top:2160px;width:1052px;text-align:center;font-size:14px;line-height:32px}
.service{position:absolute;top:2246px;width:250px;text-align:center}
.service .ico{height:84px;display:flex;justify-content:center;align-items:center}
.service h3{font-size:22px;line-height:27px;color:var(--green-dark);margin-top:20px}
.service p{font-size:14px;line-height:26px;margin-top:14px}

/* call to action */
.cta{position:absolute;left:0;top:2542px;width:1200px;height:246px;background:linear-gradient(90deg,rgba(40,40,40,.95),rgba(80,80,80,.75) 55%,rgba(60,60,60,.85)),#555}
.cta h2{position:absolute;left:74px;top:70px;color:var(--white);font-size:32px}
.cta p{position:absolute;left:74px;top:118px;width:860px;color:var(--white);font-size:16px;line-height:26px}
.cta .btn{left:959px;top:100px;width:167px;height:48px}

/* careers */
.careers-text{position:absolute;left:74px;top:2924px;width:1052px;text-align:center;font-size:14px;line-height:27px}
.careers-text p{margin-bottom:12px}
.job-row{position:absolute;left:74px;width:1052px;font-size:16px;font-weight:700;color:var(--ink);display:flex;align-items:center;gap:16px}
.job-row .sign{position:absolute;right:6px;font-size:22px}
.job-line{position:absolute;left:74px;width:1052px;height:1px;background:var(--line)}

/* contact */
.contact{position:absolute;left:0;top:3474px;width:1200px;height:629px;background:linear-gradient(90deg,#0e5a26,#1a7a35 45%,#0f6a2c 75%,#0a4a1f)}
.contact .section-title{color:var(--white);top:64px}
.contact .section-title::after{background:var(--white)}
.contact-intro{position:absolute;left:74px;top:158px;width:1052px;text-align:center;color:var(--white);font-size:14px;line-height:27px}
.info{position:absolute;left:74px;display:flex;gap:22px;color:var(--white)}
.info .ring{width:55px;height:55px;border-radius:50%;border:2px solid var(--white);display:flex;align-items:center;justify-content:center;flex:none}
.info h4{font-size:17px}
.info p{font-size:16px;line-height:24px}
.field{position:absolute;background:var(--white);font-size:13px;color:#333;padding:18px 16px}
.contact .btn{left:524px;top:505px;width:166px;height:46px}

/* footer */
.site-footer .brand{position:absolute;left:478px;top:4180px;font-size:27px}
.footer-nav{position:absolute;left:0;width:1200px;top:4267px;text-align:center;font-size:15px;font-weight:700;color:var(--ink)}
.footer-nav span{margin:0 16px}
.copyright{position:absolute;left:0;width:1200px;top:4297px;text-align:center;font-size:13px;color:var(--ink)}
.social{position:absolute;left:546px;top:4336px;display:flex;gap:22px}
.social i{display:block;width:22px;height:22px;border-radius:50%;background:var(--ink)}
</style>
</head>
<body>

<header class="site-header">
  <div class="brand"><span class="brand-dot"></span>Brook Logistics</div>
  <nav class="main-nav">
    <span>HOME</span><span>ABOUT</span><span>SERVICES</span><span>CAREERS</span>
    <span class="active">CONTACT</span><span>EN &#8964;</span>
  </nav>
</header>

<section class="hero" role="img" aria-label="Photo of a courier unloading parcel boxes from a white electric delivery van">
  <h1>BROOK LOGISTICS<br>SUSTAINABLE LAST MILE</h1>
  <div class="tagline">Because we care about our cities!</div>
  <div class="btn">CONTACT US</div>
  <div class="dots"><i></i><i></i><i></i><i></i><i></i><i></i></div>
</section>

<h2 class="section-title" style="top:732px">ABOUT US</h2>

<article class="about-card" style="left:74px">
  <div class="icon"><svg width="56" height="56" viewBox="0 0 56 56" fill="none" stroke="#fff" stroke-width="3"><circle cx="28" cy="18" r="9"/><path d="M10 48c0-10 8-17 18-17s18 7 18 17"/></svg></div>
  <h3>WHO WE ARE</h3>
  <p>Brook Logistics is a pioneer in urban green logistics and provides zero-emissions last mile delivery services for its logistics and retail clients.</p>
  <p>We take on urban parcel delivery for our clients with a 100% electric commercial vehicles fleet, fair and sustainable working conditions for our employees and an unparalleled professional and customer-focused mindset.</p>
</article>
<article class="about-card" style="left:435px">
  <div class="icon"><svg width="60" height="60" viewBox="0 0 60 60" fill="none" stroke="#fff" stroke-width="3"><circle cx="28" cy="32" r="22"/><circle cx="28" cy="32" r="14"/><circle cx="28" cy="32" r="6"/><path d="M28 32l24-22M44 10h8v8"/></svg></div>
  <h3>OUR MISSION</h3>
  <p>To satisfy consumers' ever-rising desire to buy products online, the CO2 emissions from delivery traffic will increase by 32% in the top 100 cities globally until 2030.</p>
  <p>Our clients care about our planet the same way we do, which is why Brook Logistics helps to make the planet a better place by running the most environmentally friendly urban last mile possible.</p>
</article>
<article class="about-card" style="left:795px">
  <div class="icon"><svg width="60" height="60" viewBox="0 0 60 60" fill="none" stroke="#fff" stroke-width="3"><rect x="8" y="18" width="44" height="32" rx="3"/><path d="M22 18v-6h16v6M8 30h44"/></svg></div>
  <h3>OUR VALUES</h3>
  <p>We see ourselves as a professional services company who strongly cares about the environment, its clients and their customers, as well as its employees.</p>
  <p>We believe that delivering parcels with zero emissions and providing a unique customer experience through a highly professional attitude and a great team spirit are the cornerstones for Brook Logistics to operate in today's world in a sustainable yet profitable way.</p>
</article>

<section>
  <div class="split-left"></div>
  <div class="split-right">
    <div class="brand"><span class="brand-dot"></span>Brook Logistics</div>
  </div>
  <div class="is-pill cond">BROOK LOGISTICS IS...</div>
  <div class="divider"></div>
  <div class="divider-dot"></div>
  <ul class="list struck cond" style="left:138px;top:1535px">
    <h4>AN ORDINARY PARCEL DELIVERY FIRM</h4>
    <li><svg width="16" height="16" viewBox="0 0 16 16"><circle cx="8" cy="8" r="8" fill="#fff"/><path d="M4.5 8.3l2.3 2.3 4.7-4.8" stroke="#1f8f3a" stroke-width="2" fill="none"/></svg><span>Polluting our cities</span></li>
    <li><svg width="16" height="16" viewBox="0 0 16 16"><circle cx="8" cy="8" r="8" fill="#fff"/><path d="M4.5 8.3l2.3 2.3 4.7-4.8" stroke="#1f8f3a" stroke-width="2" fill="none"/></svg><span>Always in a rush</span></li>
    <li><svg width="16" height="16" viewBox="0 0 16 16"><circle cx="8" cy="8" r="8" fill="#fff"/><path d="M4.5 8.3l2.3 2.3 4.7-4.8" stroke="#1f8f3a" stroke-width="2" fill="none"/></svg><span>Short-term oriented</span></li>
    <li><svg width="16" height="16" viewBox="0 0 16 16"><circle cx="8" cy="8" r="8" fill="#fff"/><path d="M4.5 8.3l2.3 2.3 4.7-4.8" stroke="#1f8f3a" stroke-width="2" fill="none"/></svg><span>Short-term oriented</span></li>
    <li><svg width="16" height="16" viewBox="0 0 16 16"><circle cx="8" cy="8" r="8" fill="#fff"/><path d="M4.5 8.3l2.3 2.3 4.7-4.8" stroke="#1f8f3a" stroke-width="2" fill="none"/></svg><span>Yet another parcel delivery firm</span></li>
  </ul>
  <div class="van-art" role="img" aria-label="Illustration of a white delivery van"></div>
  <ul class="list cond" style="left:670px;top:1535px">
    <h4>A PIONEERING GREEN LAST MILE</h4>
    <li><svg width="16" height="16" viewBox="0 0 16 16"><circle cx="8" cy="8" r="8" fill="#fff"/><path d="M4.5 8.3l2.3 2.3 4.7-4.8" stroke="#8dc63f" stroke-width="2" fill="none"/></svg><span>Delivering parcels emissions-free</span></li>
    <li><svg width="16" height="16" viewBox="0 0 16 16"><circle cx="8" cy="8" r="8" fill="#fff"/><path d="M4.5 8.3l2.3 2.3 4.7-4.8" stroke="#8dc63f" stroke-width="2" fill="none"/></svg><span>Putting customer experience first</span></li>
    <li><svg width="16" height="16" viewBox="0 0 16 16"><circle cx="8" cy="8" r="8" fill="#fff"/><path d="M4.5 8.3l2.3 2.3 4.7-4.8" stroke="#8dc63f" stroke-width="2" fill="none"/></svg><span>Operating the business sustainably</span></li>
    <li><svg width="16" height="16" viewBox="0 0 16 16"><circle cx="8" cy="8" r="8" fill="#fff"/><path d="M4.5 8.3l2.3 2.3 4.7-4.8" stroke="#8dc63f" stroke-width="2" fill="none"/></svg><span>Focusing on the environment, customers and employees</span></li>
    <li><svg width="16" height="16" viewBox="0 0 16 16"><circle cx="8" cy="8" r="8" fill="#fff"/><path d="M4.5 8.3l2.3 2.3 4.7-4.8" stroke="#8dc63f" stroke-width="2" fill="none"/></svg><span>A professional services company</span></li>
  </ul>
</section>

<h2 class="section-title" style="top:2080px">OUR SERVICES</h2>
<p class="services-intro">Brook Logistics provides last mile delivery services in urban areas to clients in the logistics and retail space. Our permanent employees are all highly trained and commit to highest professional standards which we continuously review and further develop with them.</p>

<div class="service" style="left:71px">
  <div class="ico"><svg width="96" height="70" viewBox="0 0 96 70" fill="none" stroke="#3aa53a" stroke-width="3"><path d="M4 10h58l16 18h14v28H4z"/><circle cx="22" cy="58" r="8" fill="#fff"/><circle cx="72" cy="58" r="8" fill="#fff"/><circle cx="34" cy="32" r="15"/><path d="M36 20l-7 13h9l-6 12"/></svg></div>
  <h3>ZERO-EMISSION<br>DELIVERY</h3>
  <p>We operate a 100% electric commercial&nbsp; vehicle fleet</p>
</div>
<div class="service" style="left:339px">
  <div class="ico"><svg width="74" height="80" viewBox="0 0 74 80" fill="none" stroke="#3aa53a" stroke-width="3"><circle cx="37" cy="20" r="12"/><path d="M25 14h24M8 78c0-18 12-30 29-30s29 12 29 30"/><rect x="26" y="54" width="22" height="18"/></svg></div>
  <h3>HIGHLY TRAINED<br>DELIVERY DRIVERS</h3>
  <p>We only employ permanently, train far above average, and live a great team spirit.</p>
</div>
<div class="service" style="left:611px">
  <div class="ico"><svg width="100" height="70" viewBox="0 0 100 70" fill="none" stroke="#3aa53a" stroke-width="3"><path d="M22 24h40v30H22zM62 34h18l12 12v8H62"/><circle cx="34" cy="58" r="7" fill="#fff"/><circle cx="78" cy="58" r="7" fill="#fff"/><circle cx="56" cy="16" r="12"/><path d="M56 10v7h6M4 34h12M8 42h10M2 50h14"/></svg></div>
  <h3>PROFESSIONAL ALL<br>AROUND</h3>
  <p>We honor our commitments and hold ourselves to the highest professional standards</p>
</div>
<div class="service" style="left:881px">
  <div class="ico"><svg width="96" height="76" viewBox="0 0 96 76" fill="none" stroke="#3aa53a" stroke-width="3"><circle cx="48" cy="18" r="10"/><circle cx="22" cy="24" r="8"/><circle cx="74" cy="24" r="8"/><path d="M30 70V44c0-8 8-14 18-14s18 6 18 14v26M6 70V48c0-6 7-10 16-10M90 70V48c0-6-7-10-16-10"/></svg></div>
  <h3>UNPARALLELED<br>CUSTOMER FOCUS</h3>
  <p>We live a customer-oriented mindset, always measuring ourselves against their experience.</p>
</div>

<section class="cta" role="img" aria-label="Dimmed photo of a courier beside a delivery van">
  <h2>Get in touch with Brook Logistics</h2>
  <p>If you got excited, or have a question about our services, our approach, our jobs or just want&nbsp; to get in touch to chat about how green logistics can make the planet a little bit better, please get in touch!</p>
  <div class="btn">CONTACT US</div>
</section>

<h2 class="section-title" style="top:2842px">CAREERS</h2>
<div class="careers-text">
  <p>If you join Brook Logistics, you join a family. We elevate one another, care for each other's wellbeing and growth, and celebrate our successes. We strongly believe growth is a team sport and that every member of the family fully contributes to the achievements of the company overall.</p>
  <p>At the heart of everything we do at Brook Logistics is a relentless focus on our mission. That's why we aim to ensure our employees can follow their own passion at the workplace, be this working in a truly collaborative and caring team, putting a smile on a customer's face or making the world a better place.</p>
  <p>While we are helping our clients grow by delivering their parcels, we are also helping all our employees grow personally and professionally. We care about our employees' happiness and wellbeing which is why we provide additional benefits like supplementary health insurance.</p>
  <p>If you are excited about joining our Brook Logistics family, please check out our open positions.</p>
</div>

<div class="job-row" style="top:3186px;color:var(--green-mid)"><svg width="16" height="16" viewBox="0 0 16 16"><circle cx="8" cy="8" r="8" fill="#2a9a3f"/><path d="M4.5 8.3l2.3 2.3 4.7-4.8" stroke="#fff" stroke-width="2" fill="none"/></svg>Full-time driver / parcel deliverer (m/f/d) for Berlin.<span class="sign">-</span></div>
<p class="abs" style="left:108px;top:3217px;font-size:14px">As a partner for our clients, we are looking for additional members of the Brook Logistics Family in Berlin as soon as possible.</p>
<div class="job-line" style="top:3254px"></div>
<div class="job-row" style="top:3269px"><svg width="16" height="16" viewBox="0 0 16 16"><circle cx="8" cy="8" r="8" fill="#222"/><path d="M4.5 8.3l2.3 2.3 4.7-4.8" stroke="#fff" stroke-width="2" fill="none"/></svg>Your tasks as a delivery driver<span class="sign">+</span></div>
<div class="job-line" style="top:3309px"></div>
<div class="job-row" style="top:3324px"><svg width="16" height="16" viewBox="0 0 16 16"><circle cx="8" cy="8" r="8" fill="#222"/><path d="M4.5 8.3l2.3 2.3 4.7-4.8" stroke="#fff" stroke-width="2" fill="none"/></svg>Required knowledge and skills<span class="sign">+</span></div>
<div class="job-line" style="top:3365px"></div>
<div class="job-row" style="top:3379px"><svg width="16" height="16" viewBox="0 0 16 16"><circle cx="8" cy="8" r="8" fill="#222"/><path d="M4.5 8.3l2.3 2.3 4.7-4.8" stroke="#fff" stroke-width="2" fill="none"/></svg>What you can expected from the Brook Logistics family:<span class="sign">+</span></div>

<section class="contact" aria-label="Contact section over a green-tinted photo of a delivery van">
  <h2 class="section-title">CONTACT</h2>
  <p class="contact-intro">We'd love to hear from you!<br>Whether you have a question about our services, our approach, our jobs or just want to get in touch to chat about how green logistics can make the planet a little bit better, our team is ready to answer your questions and enquiries.</p>
  <div class="info" style="top:270px"><span class="ring"><svg width="22" height="26" viewBox="0 0 22 26" fill="none" stroke="#fff" stroke-width="2.5"><path d="M11 24S3 15 3 9a8 8 0 0116 0c0 6-8 15-8 15z"/><circle cx="11" cy="9" r="3"/></svg></span><div><h4>LOCATION:</h4><p>Neque porro quisquam est qui<br>dolorem ipsum quia.</p></div></div>
  <div class="info" style="top:368px"><span class="ring"><svg width="26" height="20" viewBox="0 0 26 20"><rect width="26" height="20" rx="2" fill="#fff"/><path d="M1 2l12 9 12-9" stroke="#1a7a35" stroke-width="2" fill="none"/></svg></span><div><h4>EMAIL:</h4><p>hello@brooklogistics.com</p></div></div>
  <div class="info" style="top:465px"><span class="ring"><svg width="22" height="22" viewBox="0 0 24 24"><path fill="#fff" d="M6.6 10.8a15 15 0 006.6 6.6l2.2-2.2a1 1 0 011-.25 11.4 11.4 0 003.6.6 1 1 0 011 1V20a1 1 0 01-1 1A17 17 0 013 4a1 1 0 011-1h3.5a1 1 0 011 1c0 1.25.2 2.45.57 3.57a1 1 0 01-.25 1z"/></svg></span><div><h4>CALL:</h4><p>1-800-555-0142</p></div></div>
  <div class="field" style="left:524px;top:272px;width:294px;height:48px">Name</div>
  <div class="field" style="left:834px;top:272px;width:292px;height:48px">Phone No</div>
  <div class="field" style="left:524px;top:335px;width:602px;height:50px">Email Address</div>
  <div class="field" style="left:524px;top:399px;width:602px;height:92px">Message</div>
  <div class="btn">SUBMIT</div>
</section>

<footer class="site-footer">
  <div class="brand"><span class="brand-dot"></span>Brook Logistics</div>
  <nav class="footer-nav"><span>HOME</span><span>ABOUT</span><span>SERVICES</span><span>CAREERS</span><span>CONTACT</span></nav>
  <p class="copyright">Copyright © 2020 Brook Logistics. All Right Reserved&nbsp; |&nbsp; Legal Notice&nbsp; |&nbsp; Privacy Policy</p>
  <div class="social"><i></i><i></i><i></i></div>
</footer>

</body>
</html>
```